Reed & Vale NC grand opening (for BILLBOARD)

Advertising the grand opening of our cannabis/hemp shop in NC. We will sell all things hemp (flower, cartridges, disposables, edibles, creams, lotions, pet products etc...)

Requirements
Must have
• include, open starting Aug 1, but grand opening Aug 15th.
Nice to have
• Difference slogan ideas "Save some cash, buy our grass" "Find your perfect high at Reed & Vale cannabis store" "Experience Nature's Gift: Reed & Vale Cannabis Store"

```html
<!DOCTYPE html>
<html lang="en">
<head>
<meta charset="utf-8">
<title>Reed &amp; Vale Grand Opening Billboard</title>
<link rel="stylesheet" href="https://fonts.googleapis.com/css2?family=Oswald:wght@700&family=Roboto+Condensed:ital,wght@1,700&family=Roboto:wght@400;500;700&display=swap">
<style>
  :root {
    --stage: #e9ecef;
    --navy: #0f1038;
    --navy-soft: #1a2350;
    --lime: #6cc24a;
    --forest: #1b7a3c;
    --white: #ffffff;
  }
  * { margin: 0; padding: 0; box-sizing: border-box; }
  html, body { width: 1200px; height: 887px; overflow: hidden; background: var(--stage); }
  .billboard {
    position: absolute; left: 0; top: 110px; width: 1200px; height: 667px;
    background: var(--navy); overflow: hidden; color: var(--white);
    font-family: "Roboto", Arial, sans-serif; text-align: center;
  }
  .foliage-backdrop {
    position: absolute; inset: 0;
    background:
      radial-gradient(ellipse 300px 220px at 20% 55%, rgba(40,80,90,.35), transparent 70%),
      radial-gradient(ellipse 340px 260px at 80% 35%, rgba(40,80,90,.35), transparent 70%),
      radial-gradient(ellipse 260px 200px at 55% 70%, rgba(40,80,90,.25), transparent 70%);
  }
  .brand {
    position: absolute; top: 58px; left: 0; right: 0;
    display: flex; justify-content: center; align-items: center; gap: 14px;
    font-family: "Roboto", Arial, sans-serif; font-weight: 500; font-size: 62px; color: var(--lime);
  }
  .brand-dot { width: 22px; height: 22px; border-radius: 50%; background: var(--lime); }
  .headline {
    position: absolute; top: 150px; left: 0; right: 0;
    font-family: "Oswald", Impact, sans-serif; font-weight: 700; font-size: 118px;
    letter-spacing: 1px; color: var(--lime); line-height: 1;
  }
  .slogan {
    position: absolute; top: 290px; left: 0; right: 0;
    font-family: "Roboto Condensed", Arial, sans-serif; font-style: italic; font-weight: 700;
    font-size: 38px; line-height: 1.15; text-transform: uppercase;
  }
  .product-list {
    position: absolute; top: 398px; left: 0; right: 0;
    display: flex; justify-content: center; gap: 26px; list-style: none;
    font-size: 26px;
  }
  .product-list li::before { content: "•"; color: var(--lime); margin-right: 8px; }
  .open-date {
    position: absolute; top: 458px; left: 0; right: 0;
    font-weight: 500; font-size: 38px;
  }
  .open-date sup, .grand-opening sup { font-size: .55em; }
  .grand-opening {
    position: absolute; top: 522px; left: 50%; transform: translateX(-50%);
    background: var(--forest); border-radius: 40px; padding: 14px 40px;
    font-weight: 700; font-size: 42px; white-space: nowrap;
  }
  .leaves {
    position: absolute; bottom: 12px; height: 200px;
    background: radial-gradient(ellipse at 50% 100%, var(--lime) 0%, var(--forest) 55%, transparent 75%);
  }
  .leaves-left { left: 40px; width: 240px; }
  .leaves-right { right: 40px; width: 320px; height: 240px; }
  .base-band { position: absolute; left: 0; right: 0; bottom: 0; height: 12px; background: var(--lime); }
</style>
</head>
<body>
  <main class="billboard">
    <div class="foliage-backdrop" role="img" aria-label="Faint hemp leaf pattern across the navy background"></div>
    <div class="brand"><span class="brand-dot"></span><span>Reed &amp; Vale</span></div>
    <h1 class="headline">CANNABIS/HEMP SHOP</h1>
    <p class="slogan">Find your perfect<br>high at Reed &amp; Vale cannabis store</p>
    <ul class="product-list">
      <li>Flower</li><li>Cartridges</li><li>Disposables</li><li>Edibles</li><li>Creams</li><li>Lotions</li><li>Pet Products Etc</li>
    </ul>
    <p class="open-date">Open Starting Aug 1<sup>st</sup></p>
    <p class="grand-opening">GRAND OPENING AUG 15<sup>TH</sup></p>
    <div class="leaves leaves-left" role="img" aria-label="Green hemp leaves rising from the bottom left"></div>
    <div class="leaves leaves-right" role="img" aria-label="Green hemp leaves rising from the bottom right"></div>
    <div class="base-band"></div>
  </main>
</body>
</html>
```